CORE 202 fitness page promoting new gym in Harbor Point, FL

The purpose of the website is to attract new members to our new fitness facility opening in Harbor Point, Florida. The city lacks places for functional training so we want to target this market of adult/young adult fitness personal. Not just meant for fitness buffs, first timers are encouraged to begin their health/fitness journey with us. Family owned, providing a combination of fitness services include personal and small group strength training, large group fitness classes with the use of sleds, dumbbells, kettlebells, medicine balls, cones, hurdles, ladders, and punching bags. Smoothie bar inside as well. Need to deliver a clear message of what kind of workouts we do, the people we want to attract, and how to sign up. Also make it known that we have showers on site (very rare to find in fitness studios).
Target Market(s)
Fit, health conscious, business professionals
Industry/Entity Type
Fitness
Number of Pages Required
3 page
Requirements
Must have
- Bright colors that scream SIGN UP, Would like to see logo in large, a big attractive sign saying First class is free. The concept of the gym is that we educate our clients on fitness rather than throwing them blindly into working out. We want our layout to mimic a schools idea of having a curriculum (styles of class/schedule) a tuition (membership costs).
Nice to have
- Big images that promote the gym, option to have video on front page displaying workouts.

```html
<!DOCTYPE html>
<html lang="en">
<head>
<meta charset="utf-8">
<title>CORE 202 — Functional Training, Harbor Point</title>
<link href="https://fonts.googleapis.com/css2?family=Open+Sans:wght@400;600;700;800&display=swap" rel="stylesheet">
<style>
:root{
  --ink:#1d1d1f;
  --dark:#262628;
  --darker:#1a1a1b;
  --white:#ffffff;
  --grey:#6c6c70;
  --light:#f1f1f3;
  --blue:#1a8fd0;
  --yellow:#e4dd4f;
  --pink:#e96aa9;
  --line:#d9d9dc;
}
*{box-sizing:border-box;margin:0;padding:0}
html,body{width:1200px;height:2872px;overflow:hidden}
body{font-family:"Open Sans",Arial,sans-serif;color:var(--ink);background:var(--white);position:relative}

/* hero */
.hero{position:absolute;left:0;top:0;width:1200px;height:680px;background:linear-gradient(100deg,#2b2b2e 0%,#4a4a4e 35%,#222224 70%,#18181a 100%)}
.hero-athlete{position:absolute;left:90px;top:0;width:380px;height:680px;background:radial-gradient(ellipse at 50% 45%,#8a7f78 0%,#4c4744 45%,rgba(40,40,42,0) 75%)}
.brand{position:absolute;left:40px;top:34px;display:flex;align-items:center;gap:12px}
.brand-dot{width:30px;height:30px;border-radius:50%;background:var(--white)}
.brand-name{font-weight:700;font-size:32px;line-height:40px;color:var(--white);letter-spacing:1px}
.nav{position:absolute;right:92px;top:42px;display:flex;gap:40px}
.nav a{color:var(--white);text-decoration:none;font-size:14px;font-weight:600;letter-spacing:1px}
.video{position:absolute;left:524px;top:352px;width:588px;height:236px;background:linear-gradient(135deg,#7fb3cf 0%,#b9c9cf 45%,#c8a58a 100%);overflow:hidden}
.video-bar{position:absolute;left:0;top:0;right:0;height:40px;background:rgba(0,0,0,.45);color:var(--white);font-size:14px;font-weight:600;padding:10px 16px}
.video-play{position:absolute;left:264px;top:88px;width:60px;height:42px;border-radius:10px;background:rgba(20,20,20,.8)}
.video-play:after{content:"";position:absolute;left:24px;top:12px;border-left:16px solid var(--white);border-top:9px solid transparent;border-bottom:9px solid transparent}

/* offer */
.offer{position:absolute;left:0;top:680px;width:1200px;height:508px;background:var(--white)}
.offer-photo{position:absolute;left:180px;top:44px;width:380px;height:440px;background:linear-gradient(160deg,#b48a6e 0%,#7a5a48 55%,#3a2e28 100%)}
.offer-title{position:absolute;left:648px;top:166px;font-size:44px;font-weight:800;line-height:50px;color:var(--ink)}
.offer-input{position:absolute;left:648px;top:290px;width:404px;height:44px;border:1px solid var(--line);font-size:13px;color:var(--grey);padding:12px 16px;letter-spacing:1px}
.offer-btn{position:absolute;left:648px;top:352px;width:100px;height:36px;background:var(--ink);color:var(--white);font-size:12px;font-weight:700;letter-spacing:1px;text-align:center;line-height:36px}

/* educate */
.educate{position:absolute;left:0;top:1188px;width:1200px;height:344px;background:var(--blue);color:var(--white);text-align:center}
.educate-kicker{margin-top:86px;font-size:12px;font-weight:700;letter-spacing:1px}
.educate-kicker span{border-bottom:2px solid var(--white);padding-bottom:4px}
.educate-title{margin-top:18px;font-size:34px;font-weight:800;letter-spacing:1px}
.educate-text{width:780px;margin:18px auto 0;font-size:14px;line-height:24px}

/* services */
.service{position:absolute;top:1532px;width:600px;height:420px;text-align:center}
.service.smoothie{left:0;background:var(--yellow)}
.service.shower{left:600px;background:var(--pink)}
.service-icon{position:absolute;left:220px;top:52px;width:160px;height:160px;border-radius:50%;background:var(--white)}
.service-icon svg{position:absolute;left:40px;top:40px}
.service-title{position:absolute;left:0;right:0;top:254px;font-size:18px;font-weight:800;color:var(--ink)}
.service-text{position:absolute;left:150px;width:300px;top:290px;font-size:13px;line-height:21px;color:#3c3c3e}

/* testimonials */
.testimonials{position:absolute;left:0;top:1952px;width:1200px;height:576px;background:var(--white)}
.testimonials h2{position:absolute;left:0;right:0;top:52px;text-align:center;font-size:28px;font-weight:800}
.card{position:absolute;top:128px;height:368px;background:var(--light)}
.card.quote{left:100px;width:308px;background:var(--white);border:1px solid var(--line)}
.card-mark{position:absolute;left:138px;top:110px;font-size:48px;font-weight:800;color:#bfbfc3}
.card-quote{position:absolute;left:40px;right:40px;top:172px;text-align:center;font-size:12px;line-height:20px;color:var(--grey)}
.card.person{width:308px}
.card.p1{left:448px}.card.p2{left:788px}
.avatar{position:absolute;left:74px;top:40px;width:160px;height:160px;border-radius:50%;border:6px solid var(--white)}
.p1 .avatar{background:linear-gradient(160deg,#d9b49a,#6c5a4e)}
.p2 .avatar{background:linear-gradient(160deg,#c98f6d,#4e3a30)}
.person-name{position:absolute;left:0;right:0;top:236px;text-align:center;font-size:16px;font-weight:800}
.person-role{position:absolute;left:0;right:0;top:262px;text-align:center;font-size:11px;font-weight:700;color:var(--grey);letter-spacing:1px}

/* footer */
.footer{position:absolute;left:0;top:2528px;width:1200px;height:292px;background:var(--dark);color:var(--white)}
.footer h4{font-size:13px;font-weight:800;letter-spacing:1px;margin-bottom:14px}
.hours{position:absolute;left:96px;top:52px;font-size:12px;line-height:24px}
.hours li{list-style:none;display:flex;width:220px;justify-content:space-between}
.contact{position:absolute;left:456px;top:52px}
.contact-row{display:flex;gap:18px;margin-bottom:16px;font-size:12px;line-height:18px}
.contact-row b{display:block;font-weight:800}
.follow{position:absolute;left:860px;top:52px}
.social{display:flex;gap:10px}
.social span{width:26px;height:26px;background:#8c8c90}
.footer-photo{position:absolute;left:1020px;top:0;width:180px;height:292px;background:linear-gradient(200deg,#6a5248 0%,#3a302c 60%,#262628 100%)}
.copyright{position:absolute;left:0;top:2820px;width:1200px;height:52px;background:var(--darker);color:#b9b9bd;font-size:12px;text-align:center;line-height:52px}
</style>
</head>
<body>

<header class="hero">
  <div class="hero-athlete" role="img" aria-label="Woman training with a dumbbell in a dark gym"></div>
  <div class="brand"><span class="brand-dot"></span><span class="brand-name">CORE 202</span></div>
  <nav class="nav"><a href="#">HOME</a><a href="#">ABOUT US</a><a href="#">CLASSES</a><a href="#">MEMBERSHIPS</a><a href="#">CONTACT US</a></nav>
  <div class="video" role="img" aria-label="Workout video preview of a woman stretching on a beach">
    <div class="video-bar">Circuit Session &bull; Kettlebell Basics</div>
    <div class="video-play"></div>
  </div>
</header>

<section class="offer">
  <div class="offer-photo" role="img" aria-label="Athlete lifting a kettlebell over bold diagonal stripes"></div>
  <h1 class="offer-title">CORE 202<br>FIRST CLASS FREE</h1>
  <div class="offer-input">ENTER YOUR EMAIL</div>
  <div class="offer-btn">SIGN UP</div>
</section>

<section class="educate">
  <p class="educate-kicker"><span>GYM IN HARBOR POINT, FLORIDA</span></p>
  <h2 class="educate-title">EDUCATE YOUR BODY</h2>
  <p class="educate-text">Functional training studio built for busy people who want real results and lasting habits. Our coaches teach every movement, explain why it matters and build your plan step by step, so you never train blindly. Learn the skills, follow the curriculum and grow stronger with us.</p>
</section>

<section class="service smoothie">
  <div class="service-icon">
    <svg width="80" height="80" viewBox="0 0 80 80"><path d="M22 24h36l-6 48H28z" fill="#f3b23c" stroke="#1d1d1f" stroke-width="3"/><path d="M40 24 50 6" stroke="#1d1d1f" stroke-width="3"/><circle cx="62" cy="22" r="8" fill="#e4dd4f" stroke="#1d1d1f" stroke-width="3"/></svg>
  </div>
  <h3 class="service-title">SMOOTHIE BAR</h3>
  <p class="service-text">Refuel right after class with fresh protein shakes and fruit blends made to order at our bar. Healthy choices that support every training goal you set.</p>
</section>

<section class="service shower">
  <div class="service-icon">
    <svg width="80" height="80" viewBox="0 0 80 80"><path d="M14 30a26 26 0 0 1 52 0z" fill="#e96aa9" stroke="#1d1d1f" stroke-width="3"/><path d="M40 4v12" stroke="#1d1d1f" stroke-width="3"/><g fill="#1a8fd0"><circle cx="24" cy="44" r="4"/><circle cx="40" cy="46" r="4"/><circle cx="56" cy="44" r="4"/><circle cx="30" cy="60" r="4"/><circle cx="50" cy="60" r="4"/></g></svg>
  </div>
  <h3 class="service-title">SHOWER SERVICE</h3>
  <p class="service-text">Clean private showers on site, so you can train before work and head straight to the office. A rare comfort in studios, and free for all members.</p>
</section>

<section class="testimonials">
  <h2>TESTIMONIALS</h2>
  <div class="card quote">
    <div class="card-mark">&ldquo;</div>
    <p class="card-quote">The coaches explained every drill and why we do it. After two months I feel stronger, move better and actually enjoy my morning sessions before heading to work.</p>
  </div>
  <div class="card person p1">
    <div class="avatar" role="img" aria-label="Portrait of a member"></div>
    <div class="person-name">M. REYES</div>
    <div class="person-role">STUDENT</div>
  </div>
  <div class="card person p2">
    <div class="avatar" role="img" aria-label="Portrait of a member"></div>
    <div class="person-name">D. HOLLAND</div>
    <div class="person-role">STUDENT</div>
  </div>
</section>

<footer class="footer">
  <div class="hours">
    <h4>BUSINESS HOURS</h4>
    <ul>
      <li><span>MONDAY</span><span>5:00 AM - 8:30 PM</span></li>
      <li><span>TUESDAY</span><span>5:00 AM - 8:30 PM</span></li>
      <li><span>WEDNESDAY</span><span>5:00 AM - 8:30 PM</span></li>
      <li><span>THURSDAY</span><span>5:00 AM - 8:30 PM</span></li>
      <li><span>FRIDAY</span><span>5:00 AM - 7:00 PM</span></li>
      <li><span>SATURDAY</span><span>8:00 AM - 1:00 PM</span></li>
      <li><span>SUNDAY</span><span>9:00 AM - 12:00 PM</span></li>
    </ul>
  </div>
  <div class="contact">
    <div class="contact-row">
      <svg width="24" height="24" viewBox="0 0 24 24"><path d="M12 2a7 7 0 0 0-7 7c0 5 7 13 7 13s7-8 7-13a7 7 0 0 0-7-7z" fill="none" stroke="#fff" stroke-width="2"/><circle cx="12" cy="9" r="2.5" fill="#fff"/></svg>
      <div><b>VISIT US</b>480 Harbor Lane, Harbor Point,<br>FL 33004</div>
    </div>
    <div class="contact-row">
      <svg width="24" height="24" viewBox="0 0 24 24"><path d="M5 3h4l2 5-3 2a12 12 0 0 0 6 6l2-3 5 2v4a2 2 0 0 1-2 2A17 17 0 0 1 3 5a2 2 0 0 1 2-2z" fill="none" stroke="#fff" stroke-width="2"/></svg>
      <div><b>CALL US</b>(954) 555-0142</div>
    </div>
    <div class="contact-row">
      <svg width="24" height="24" viewBox="0 0 24 24"><rect x="2" y="5" width="20" height="14" fill="none" stroke="#fff" stroke-width="2"/><path d="M2 6l10 7 10-7" fill="none" stroke="#fff" stroke-width="2"/></svg>
      <div><b>MAIL US</b>hello@core202gym.com</div>
    </div>
  </div>
  <div class="follow">
    <h4>FOLLOW US</h4>
    <div class="social"><span></span><span></span></div>
  </div>
  <div class="footer-photo" role="img" aria-label="Athlete training with a barbell"></div>
</footer>
<div class="copyright">Copyright &copy; 2018 CORE 202 Gym. All rights reserved.</div>

</body>
</html>
```